Web Developer Needs a Business Card Design

I need a personal business card design that represents me as a web developer for potential employers. I would like the background to be a dark color on the front for contrast with my logo and name. The back will have all my information along with a smaller version of the logo. I want something with a modern look and feel, not too conservative. This will be used for potential employers and freelance work.

Industry/Entity Type

Business

Contact Information for Business Card

Front should have my logo and name. The back should have all my personal information which would include: name: Tom Brevardi, phone: 570-614-9083, email: tombrevardi@mailwisp.com, website url: www.tombrevardi.com, logo, web developer.

Font styles to use
Sans Serif

Requirements
Must have
• Must include my logo. The color palette base color will be the logo color.

```html
<!DOCTYPE html>
<html lang="en">
<head>
<meta charset="utf-8">
<title>Tom Brevardi – Business Card</title>
<link rel="stylesheet" href="https://fonts.googleapis.com/css2?family=Michroma&family=Open+Sans:wght@400;600;700&display=swap">
<style>
  :root {
    --page-bg: #eeeff0;
    --card-white: #ffffff;
    --brand-dark: #035b42;
    --brand-light: #43b97a;
    --brand-faint: #e6f4ee;
    --ink: #1d1d1d;
    --ink-soft: #555b58;
    --front-text: #d9e6e0;
  }
  * { box-sizing: border-box; margin: 0; padding: 0; }
  html, body {
    width: 1200px; height: 905px; overflow: hidden;
    background: var(--page-bg);
    font-family: "Open Sans", sans-serif;
  }
  .stage {
    position: relative; width: 1200px; height: 905px;
    display: flex; align-items: center; justify-content: center; gap: 40px;
  }
  .card {
    position: relative; width: 520px; height: 297px;
    border-radius: 4px; overflow: hidden;
    box-shadow: 0 10px 28px rgba(0,0,0,.12);
  }

  /* Back: contact side */
  .card-back { background: var(--card-white); }
  .card-back .watermark {
    position: absolute; right: 40px; top: 60px; width: 250px; height: 250px;
  }
  .card-back .band {
    position: absolute; left: 0; top: 0; width: 300px; height: 112px;
    background: var(--brand-light);
    border-bottom-right-radius: 30px;
    display: flex; align-items: center; justify-content: center;
  }
  .mark {
    display: flex; align-items: center; gap: 8px;
    font-family: "Open Sans", sans-serif; font-weight: 700;
  }
  .mark-dot { border-radius: 50%; flex: none; }
  .band .mark { color: var(--card-white); font-size: 20px; }
  .band .mark-dot { width: 22px; height: 22px; border: 3px solid var(--card-white); }
  .identity { position: absolute; left: 28px; top: 124px; }
  .identity .name { color: var(--brand-light); font-weight: 700; font-size: 20px; line-height: 1.1; }
  .identity .role { color: var(--ink-soft); font-size: 13px; }
  .contacts { position: absolute; left: 270px; top: 150px; }
  .contact { display: flex; align-items: center; gap: 9px; color: var(--ink); }
  .contact svg { flex: none; }
  .contact.phone { font-weight: 700; font-size: 19px; margin-bottom: 24px; }
  .contact.line { font-size: 11.5px; margin-bottom: 8px; }

  /* Front: brand side */
  .card-front {
    background: var(--brand-dark);
    display: flex; align-items: center; justify-content: center; gap: 24px;
  }
  .card-front .wordmark {
    font-family: "Michroma", sans-serif; font-size: 15px;
    letter-spacing: .18em; text-transform: uppercase; color: var(--front-text);
  }
  .card-front .mark { color: var(--card-white); font-size: 22px; }
  .card-front .mark-dot { width: 26px; height: 26px; border: 3px solid var(--card-white); }
</style>
</head>
<body>
<main class="stage">

  <section class="card card-back" aria-label="Business card, contact side">
    <svg class="watermark" viewBox="0 0 250 250" aria-hidden="true">
      <circle cx="125" cy="125" r="110" fill="none" stroke="var(--brand-faint)" stroke-width="16"/>
    </svg>
    <div class="band">
      <div class="mark"><span class="mark-dot"></span>Brevardi</div>
    </div>
    <div class="identity">
      <p class="name">Tom Brevardi</p>
      <p class="role">web developer</p>
    </div>
    <div class="contacts">
      <p class="contact phone">
        <svg width="16" height="16" viewBox="0 0 16 16" aria-hidden="true">
          <rect x="0.5" y="0.5" width="15" height="15" rx="2" fill="none" stroke="var(--ink)"/>
          <path d="M5 3.5l2 2-1 1.2c.6 1.3 1.5 2.2 2.8 2.8l1.2-1 2 2-1.3 1.5C7.5 11.5 4.5 8.5 3.5 4.8z" fill="var(--ink)"/>
        </svg>
        570-614-9083
      </p>
      <p class="contact line">
        <svg width="10" height="10" viewBox="0 0 10 10" aria-hidden="true">
          <circle cx="5" cy="5" r="4.3" fill="none" stroke="var(--ink)" stroke-width="1.2"/>
          <path d="M.7 5h8.6M5 .7c-2.4 2.6-2.4 6 0 8.6M5 .7c2.4 2.6 2.4 6 0 8.6" fill="none" stroke="var(--ink)" stroke-width=".8"/>
        </svg>
        www.tombrevardi.com
      </p>
      <p class="contact line">
        <svg width="10" height="10" viewBox="0 0 10 10" aria-hidden="true">
          <circle cx="5" cy="5" r="4.3" fill="none" stroke="var(--ink)" stroke-width="1.2"/>
          <circle cx="5" cy="5" r="1.6" fill="var(--ink)"/>
        </svg>
        tombrevardi@mailwisp.com
      </p>
    </div>
  </section>

  <section class="card card-front" aria-label="Business card, brand side">
    <p class="wordmark">Tom Brevardi</p>
    <div class="mark"><span class="mark-dot"></span>Brevardi</div>
  </section>

</main>
</body>
</html>
```